Data Analytics Irish company needs Stationery Design

We need a stationery design for our data analytics company based in Dublin called 'Numbryx': we develop innovative web-based corporate applications exploiting advanced Machine Learning and Data Mining techniques.
Like the animal that inspired our company name, the final design should communicate intelligence and passion; on the other hand, we want to keep the highest professional appeal.
We love our current logo and we have tried out several color variations: we prefer solutions (see the logo attached) with white design and dark backgrounds, but we will also be glad to see some designs that follow the colors of the palette of the attached web screenshot.

```html
<!DOCTYPE html>
<html lang="en">
<head>
<meta charset="utf-8">
<title>Numbryx Presentation Folder</title>
<link rel="stylesheet" href="https://fonts.googleapis.com/css2?family=Exo+2:wght@500&display=swap">
<style>
  :root {
    --bg-light: #f2f2f2;
    --bg-dark: #b9b9b9;
    --brand-deep: #0d4f93;
    --brand-mid: #1868b0;
    --brand-glow: #2a7fc2;
    --paper: #ffffff;
    --paper-shade: #e6e6e6;
    --ink-grey: #555555;
  }
  * { margin: 0; padding: 0; box-sizing: border-box; }
  html, body { width: 1200px; height: 900px; overflow: hidden; }
  body {
    position: relative;
    font-family: "Exo 2", sans-serif;
    background: radial-gradient(ellipse at 50% 35%, var(--bg-light) 0%, #dcdcdc 55%, var(--bg-dark) 100%);
  }

  /* Folder cover */
  .folder-cover {
    position: absolute;
    left: 108px; top: 140px;
    width: 290px; height: 535px;
    background: radial-gradient(ellipse at 40% 85%, var(--brand-glow) 0%, var(--brand-mid) 35%, var(--brand-deep) 80%);
  }
  .brand-lockup {
    position: absolute;
    display: flex; flex-direction: column; align-items: center;
    color: var(--paper);
    font-weight: 500;
  }
  .brand-lockup .brand-dot {
    border-radius: 50%;
    background: currentColor;
  }
  .folder-cover .brand-lockup { left: 0; right: 0; top: 320px; }
  .folder-cover .brand-dot { width: 44px; height: 44px; margin-bottom: 14px; }
  .folder-cover .brand-name { font-size: 34px; letter-spacing: 0.5px; }

  /* Inside spread */
  .folder-spread {
    position: absolute;
    left: 550px; top: 146px;
    width: 545px; height: 504px;
    display: flex;
  }
  .spread-panel {
    position: relative;
    width: 50%; height: 100%;
    background: linear-gradient(180deg, var(--paper) 0%, var(--paper-shade) 100%);
  }
  .spread-panel + .spread-panel { border-left: 1px solid #cfcfcf; }
  .pocket {
    position: absolute;
    left: 0; right: 0; bottom: 0;
    height: 158px;
    background: radial-gradient(ellipse at 45% 80%, var(--brand-glow) 0%, var(--brand-mid) 55%, var(--brand-deep) 100%);
  }
  .pocket .brand-lockup { left: 0; right: 0; top: 52px; }
  .pocket .brand-dot { width: 22px; height: 22px; margin-bottom: 7px; }
  .pocket .brand-name { font-size: 18px; }

  .business-card {
    position: absolute;
    left: 70px; top: 34px;
    width: 140px; height: 82px;
    background: var(--paper);
    clip-path: polygon(12px 0, 100% 0, 100% 100%, 0 100%, 0 12px);
    font-size: 7px;
    color: var(--ink-grey);
  }
  .business-card .card-mark {
    position: absolute; left: 14px; top: 14px;
    width: 18px; height: 18px; border-radius: 50%;
    background: var(--brand-mid);
  }
  .business-card .card-contact {
    position: absolute; right: 10px; top: 46px;
    line-height: 11px; text-align: left;
  }

  /* Standalone brand mark */
  .brand-signoff {
    position: absolute;
    right: 60px; top: 742px;
    color: var(--brand-mid);
  }
  .brand-signoff .brand-dot { width: 54px; height: 54px; margin-bottom: 12px; }
  .brand-signoff .brand-name { font-size: 44px; letter-spacing: 0.5px; }
</style>
</head>
<body>
  <section class="folder-cover" aria-label="Folder front cover">
    <div class="brand-lockup">
      <span class="brand-dot"></span>
      <span class="brand-name">Numbryx</span>
    </div>
  </section>

  <section class="folder-spread" aria-label="Folder inside spread">
    <div class="spread-panel">
      <div class="pocket">
        <div class="brand-lockup">
          <span class="brand-dot"></span>
          <span class="brand-name">Numbryx</span>
        </div>
      </div>
    </div>
    <div class="spread-panel">
      <div class="pocket">
        <div class="business-card">
          <span class="card-mark"></span>
          <div class="card-contact">
            <p>000 000 000</p>
            <p>www.numbryx.ie</p>
          </div>
        </div>
      </div>
    </div>
  </section>

  <div class="brand-lockup brand-signoff">
    <span class="brand-dot"></span>
    <span class="brand-name">Numbryx</span>
  </div>
</body>
</html>
```